Webpage Design Layout for Thanksgiving/App Charity

Hi,

I am putting together a website called http://kindlyloop.example with the intention of getting app developers to giveaway their usual thanksgiving discount to a charity rather than to the customer.

I am looking for a one page design (not coded) that will have;

1. A header and small description of the idea. For example;

"KindlyLoop - Sharing Makes Ripples"

KindlyLoop is a movement that lets developers and users pass on the usual Thanksgiving discounts to people and communities who need it most. Buy your favourite apps from the links below and 40% of the price goes directly to charity"

2. A small section outlining the charity (not yet selected) with a link to learn more and a 'Play Video' button. I'd like to include a video of the charity.

3. A grid showing the available apps with an 'About' button and 'Buy Now' button

4. a FAQ underneath the apps

5. Some kind of prominent "Money raised" bar that will go near the top of the page

6. A footer section with contact info, mailing list sign up.

7. A countdown timer near the top that will countdown until the charity is over

8. A logo that would represent Apps + Thanksgiving

Obviously since this ties in with thanksgiving and apps I'd like to make it a fun turkey or thanksgiving themed page.

Please use Google Fonts and make sure to have the rights to any images used.

Target Market(s)

I want to appeal to every day phone and computer users. It should be a fun page but that also display credibility and confidence for purchasers/visitors.

Industry/Entity Type

Software

Number of Pages Required

1 page

Requirements
Must have
• Just a fun page that displays credibility and the importance of the idea

```html
<!DOCTYPE html>
<html lang="en">
<head>
<meta charset="utf-8">
<title>KindlyLoop - Sharing Makes Ripples</title>
<link rel="stylesheet" href="https://fonts.googleapis.com/css2?family=Raleway:wght@200;300;400;500;600;700&display=swap">
<style>
:root{
  --pink:#f2185c;
  --pink-soft:#f04a78;
  --pink-light:#f7a3b9;
  --green:#80c342;
  --ink:#1c1c1c;
  --grey:#d4d4d4;
  --rule:#9a9a9a;
  --black:#050505;
  --white:#ffffff;
  --icon:#8a7d6e;
}
*{box-sizing:border-box;margin:0;padding:0}
html,body{width:1200px;height:4700px;overflow:hidden;background:var(--white)}
body{font-family:"Raleway",sans-serif;color:var(--ink);position:relative}
.section{position:absolute;left:0;width:1200px}
.center{position:absolute;left:0;width:1200px;text-align:center}
.abs{position:absolute}
.rule{position:absolute;left:0;width:1200px;height:3px;background:var(--rule)}
.underline{position:absolute;height:3px;background:var(--green)}

/* hero */
.hero{top:0;height:555px;background:linear-gradient(180deg,#3a3431 0%,#5a4a40 45%,#2c2623 100%)}
.hero-photo{position:absolute;inset:0}
.brand{position:absolute;left:70px;top:14px;display:flex;align-items:center;gap:12px;color:#f2603f;font-weight:600;font-size:40px;letter-spacing:2px}
.brand-dot{width:34px;height:34px;border-radius:50%;background:#f2603f}
.nav{position:absolute;top:22px;right:70px;display:flex;gap:48px;font-size:22px;color:var(--white);letter-spacing:1px}
.nav .active{border-bottom:2px solid var(--white);padding-bottom:4px}
.nav-line{position:absolute;top:72px;left:530px;right:40px;height:2px;background:rgba(255,255,255,.5)}
.hero-name{top:132px;font-size:58px;font-weight:300;color:var(--pink)}
.hero-tag{top:198px;font-size:56px;font-weight:300;color:var(--white)}
.hero-line{position:absolute;top:268px;left:340px;width:520px;height:3px;background:var(--green)}
.hero-badge{position:absolute;top:285px;left:552px;width:96px;height:96px;border-radius:50%;background:var(--pink);color:var(--white);font-size:32px;font-weight:500;display:flex;align-items:center;justify-content:center}
.hero-sub{top:395px;font-size:32px;font-style:italic;font-weight:300;color:var(--white)}
.arrow{position:absolute;top:250px;width:44px;height:76px;background:var(--pink);display:flex;align-items:center;justify-content:center}
.arrow.left{left:0;border-radius:0 38px 38px 0}
.arrow.right{right:0;border-radius:38px 0 0 38px}

/* about */
.about{top:555px;height:316px;background:var(--pink-soft)}
.about svg{position:absolute;inset:0}
.about h2{top:50px;font-size:48px;font-weight:500;letter-spacing:8px;color:var(--ink)}
.about p{position:absolute;top:130px;left:235px;width:730px;text-align:center;font-size:20px;line-height:27px;color:#2a1a20}

/* rising */
.rising{top:871px;height:485px}
.rising h2{top:55px;font-size:48px;font-weight:300}
.rising .amount{top:140px;font-size:48px;font-weight:300;color:var(--pink)}
.bar{position:absolute;top:287px;left:116px;width:971px;height:50px;border-radius:25px;background:var(--grey);overflow:hidden}
.bar-fill{width:57%;height:100%;background:repeating-linear-gradient(135deg,#8ccb4a 0 12px,#74b63b 12px 24px)}
.pin{position:absolute;top:210px;left:648px}
.stat{position:absolute;top:360px;font-size:21px;line-height:26px}
.stat b{font-weight:400;color:var(--pink)}

/* charity */
.charity{top:1356px;height:881px}
.charity h2{top:60px;font-size:46px;font-weight:300}
.charity p{position:absolute;top:150px;left:160px;width:880px;text-align:center;font-size:16px;line-height:21px}
.video{position:absolute;top:214px;left:0;width:1200px;height:492px;background:linear-gradient(135deg,#6b5a3c 0%,#a2573f 45%,#3c3a2a 100%)}
.play{position:absolute;top:164px;left:527px}
.btn{position:absolute;display:flex;align-items:center;justify-content:center;color:var(--white);font-size:20px;letter-spacing:1px}
.btn.round{border-radius:30px}
.btn.pink{background:var(--pink)}
.btn.green{background:var(--green);color:#1f3a0e}

/* apps */
.apps{top:2237px;height:921px}
.apps h2{top:60px;font-size:46px;font-weight:300}
.app-icon{position:absolute;width:132px;height:132px;border-radius:18px;background:var(--icon)}
.app-text{position:absolute;width:310px;font-size:15px;line-height:20px}

/* faq */
.faq{top:3158px;height:508px}
.faq h2{top:56px;font-size:46px;font-weight:300;letter-spacing:8px}
.faq-list{position:absolute;top:185px;left:144px;font-size:21px;line-height:34px}
.faq-list dt{font-weight:700}

/* contact */
.touch{top:3666px;height:444px;background:linear-gradient(180deg,var(--pink-light) 0%,var(--pink-light) 62%,#ffffff 100%)}
.touch h2{top:45px;font-size:44px;font-weight:300;letter-spacing:6px;color:var(--pink)}
.touch .sub{top:140px;font-size:21px;letter-spacing:4px;line-height:30px;color:#3a2a2e}
.news-input{position:absolute;top:238px;left:263px;width:470px;height:75px;background:#d9b5a2;border-radius:6px;color:#f2dfd4;font-size:20px;letter-spacing:4px;display:flex;align-items:center;padding-left:20px}

/* footer */
.footer{top:4110px;height:590px;background:var(--black);color:var(--white)}
.field{position:absolute;border:2px solid #cfcfcf;color:#9d9d9d;font-size:20px;letter-spacing:4px;padding:0 30px;display:flex;align-items:center}
.field.tall{align-items:flex-start;padding-top:22px}
.footer h3{position:absolute;left:796px;font-size:30px;font-weight:400;letter-spacing:5px;color:var(--pink)}
.footer .info{position:absolute;left:796px;font-size:19px;letter-spacing:2px;line-height:24px}
.socials{position:absolute;left:796px;top:292px;display:flex;gap:18px}
.socials span{width:28px;height:28px;background:var(--white);border-radius:4px}
.copy-rule{position:absolute;top:533px;left:0;width:1200px;height:2px;background:#bdbdbd}
.copy{position:absolute;top:549px;left:0;width:1200px;text-align:center;font-size:22px;letter-spacing:1px}
</style>
</head>
<body>

<header class="section hero">
  <div class="hero-photo" role="img" aria-label="Photo of a smiling child in warm dusk light"></div>
  <div class="brand"><span class="brand-dot"></span>KindlyLoop</div>
  <nav class="nav"><span class="active">ABOUT</span><span>CHARITY</span><span>APPS</span><span>FAQ</span><span>CONTACT</span></nav>
  <div class="nav-line"></div>
  <div class="arrow left"><svg width="20" height="30" viewBox="0 0 20 30"><path d="M15 3 L4 15 L15 27" fill="none" stroke="#fff" stroke-width="4"/></svg></div>
  <div class="arrow right"><svg width="20" height="30" viewBox="0 0 20 30"><path d="M5 3 L16 15 L5 27" fill="none" stroke="#fff" stroke-width="4"/></svg></div>
  <h1 class="center hero-name">KindlyLoop</h1>
  <div class="center hero-tag">Give Where It Means</div>
  <div class="hero-line"></div>
  <div class="hero-badge">40%</div>
  <div class="center hero-sub">of all purchase go to Charity</div>
</header>

<section class="section about">
  <svg width="1200" height="316" viewBox="0 0 1200 316"><polygon points="720,316 1200,0 1200,316" fill="#f56088"/><polygon points="860,0 1200,0 1200,0 760,316 700,316" fill="#ee3d6e"/></svg>
  <h2 class="center">ABOUT US</h2>
  <p>KindlyLoop is a movement that lets developers and users pass on the usual Thanksgiving discounts to people and communities who need it most. Buy your favourite apps from the links below and 40% of the price goes directly to charity.</p>
</section>

<section class="section rising">
  <h2 class="center">WE'RE RISING</h2>
  <div class="underline" style="top:132px;left:520px;width:160px"></div>
  <div class="center amount">$ 10,000</div>
  <svg class="pin" width="44" height="62" viewBox="0 0 44 62"><path d="M22 60 C10 40 2 32 2 21 A20 20 0 0 1 42 21 C42 32 34 40 22 60Z" fill="var(--pink)"/><circle cx="22" cy="21" r="8" fill="#fff"/></svg>
  <div class="bar"><div class="bar-fill"></div></div>
  <div class="stat" style="left:116px"><b>$4700</b><br>Still Needed</div>
  <div class="stat" style="left:612px"><b>53%</b><br>of goal met</div>
  <div class="stat" style="left:978px;text-align:right"><b>2 days</b><br>Remaining</div>
  <div class="rule" style="top:482px"></div>
</section>

<section class="section charity">
  <h2 class="center">Charity Brighter Tomorrow Fund</h2>
  <p>Working towards a world where every child attains the right to survival, protection, development and participation. Inspiring breakthroughs in the way the world treats children to achieve immediate and lasting change.</p>
  <div class="video" role="img" aria-label="Video still of two children with goats outdoors">
    <svg class="play" width="146" height="146" viewBox="0 0 146 146"><circle cx="73" cy="73" r="70" fill="none" stroke="rgba(255,255,255,.75)" stroke-width="5"/><polygon points="56,40 56,106 108,73" fill="rgba(255,255,255,.75)"/></svg>
  </div>
  <div class="btn round pink" style="top:763px;left:508px;width:184px;height:48px">LEARN MORE</div>
  <div class="rule" style="top:878px"></div>
</section>

<section class="section apps">
  <h2 class="center">AVAILABLE APPS</h2>
  <div class="underline" style="top:130px;left:520px;width:160px"></div>

  <div class="app-icon" style="top:175px;left:72px" role="img" aria-label="App icon placeholder"></div>
  <p class="app-text" style="top:180px;left:229px">Explore randomly generated worlds and build amazing things from the simplest of homes to the grandest of castles. Play in creative mode with unlimited resources or mine deep into the world in survival mode, crafting weapons and armor to fend off the dangerous mobs.</p>
  <div class="app-icon" style="top:175px;left:617px" role="img" aria-label="App icon placeholder"></div>
  <p class="app-text" style="top:180px;left:774px">Explore randomly generated worlds and build amazing things from the simplest of homes to the grandest of castles. Play in creative mode with unlimited resources or mine deep into the world in survival mode, crafting weapons and armor to fend off the dangerous mobs.</p>
  <div class="btn round pink" style="top:373px;left:81px;width:188px;height:48px">LEARN MORE</div>
  <div class="btn round green" style="top:373px;left:304px;width:182px;height:48px">BUY NOW</div>
  <div class="btn round pink" style="top:373px;left:626px;width:188px;height:48px">LEARN MORE</div>
  <div class="btn round green" style="top:373px;left:849px;width:182px;height:48px">BUY NOW</div>

  <div class="app-icon" style="top:461px;left:72px" role="img" aria-label="App icon placeholder"></div>
  <p class="app-text" style="top:466px;left:229px">Explore randomly generated worlds and build amazing things from the simplest of homes to the grandest of castles. Play in creative mode with unlimited resources or mine deep into the world in survival mode, crafting weapons and armor to fend off the dangerous mobs.</p>
  <div class="app-icon" style="top:461px;left:617px" role="img" aria-label="App icon placeholder"></div>
  <p class="app-text" style="top:466px;left:774px">Explore randomly generated worlds and build amazing things from the simplest of homes to the grandest of castles. Play in creative mode with unlimited resources or mine deep into the world in survival mode, crafting weapons and armor to fend off the dangerous mobs.</p>
  <div class="btn round pink" style="top:656px;left:81px;width:188px;height:48px">LEARN MORE</div>
  <div class="btn round green" style="top:656px;left:304px;width:182px;height:48px">BUY NOW</div>
  <div class="btn round pink" style="top:656px;left:626px;width:188px;height:48px">LEARN MORE</div>
  <div class="btn round green" style="top:656px;left:849px;width:182px;height:48px">BUY NOW</div>

  <div class="btn pink" style="top:780px;left:467px;width:266px;height:69px">SEE MORE APPS</div>
  <div class="rule" style="top:918px"></div>
</section>

<section class="section faq">
  <h2 class="center">FAQS</h2>
  <div class="underline" style="top:131px;left:545px;width:110px"></div>
  <dl class="faq-list">
    <dt>How much money goes charity?</dt>
    <dd>40% off all purchases that go through the Buy Now button for each app goes to charity</dd>
    <dt>What Charity will the money go to?</dt>
    <dd>40% off all purchases that go through the Buy Now button for each app goes to charity</dd>
  </dl>
  <div class="btn pink" style="top:370px;left:501px;width:201px;height:66px">ASK NOW</div>
</section>

<section class="section touch">
  <h2 class="center">GET IN TOUCH</h2>
  <div class="underline" style="top:110px;left:470px;width:260px;background:var(--pink)"></div>
  <div class="center sub">FOR LATEST INFORMAION AND CHARITY<br>SUBSCRIBE TO OUR NEWSLETTER</div>
  <div class="news-input">ENTER YOUR EMAIL</div>
  <div class="btn round pink" style="top:238px;left:752px;width:188px;height:75px;letter-spacing:4px">SEND</div>
</section>

<footer class="section footer">
  <div class="field" style="top:66px;left:75px;width:298px;height:69px">FIRST NAME</div>
  <div class="field" style="top:66px;left:395px;width:297px;height:69px">LAST NAME</div>
  <div class="field" style="top:157px;left:75px;width:617px;height:69px">ENTER YOUR EMAIL ADDRESS</div>
  <div class="field tall" style="top:251px;left:75px;width:617px;height:160px">ENTER YOUR MESSAGE</div>
  <div class="field" style="top:442px;left:260px;width:226px;height:69px;justify-content:center;padding:0">SEND</div>

  <h3 style="top:40px">ADDRESS</h3>
  <p class="info" style="top:88px">1180 Maple Row, Riverton<br>Alberta</p>
  <svg class="abs" style="left:796px;top:150px" width="28" height="28" viewBox="0 0 28 28"><rect width="28" height="28" rx="4" fill="#fff"/><path d="M8 6 L12 6 L13 11 L11 12.5 C12 15 13.5 16.5 15.5 17 L17 15 L22 16 L22 20 C15 21 7 13 8 6Z" fill="#000"/></svg>
  <p class="info" style="top:190px">555-014-2291</p>
  <h3 style="top:232px">Follow us</h3>
  <div class="socials"><span></span><span></span><span></span><span></span><span></span></div>

  <div class="copy-rule"></div>
  <p class="copy">© Copyright - 2017 kindlyloop.example All Rights Reserved</p>
</footer>

</body>
</html>
```